BrickaFun Business Card

We need a business card design for our company. We sell construction-themed amusement rides for kids.

Contact Information for Business Card

Contact info on business card should include:
Dale Hurst
Co-Founder & COO
(833) 517-BRICKAF
Dale@brickafun.com
www.brickafun.com

```html
<!DOCTYPE html>
<html lang="en">
<head>
<meta charset="utf-8">
<title>BrickaFun Business Card</title>
<link href="https://fonts.googleapis.com/css2?family=Open+Sans:wght@400;600;700&display=swap" rel="stylesheet">
<style>
  :root {
    --backdrop: #efeceb;
    --card: #ffffff;
    --ink: #111111;
    --brand: #f07a1e;
    --yellow-light: #f5e82c;
    --yellow-deep: #f0a51a;
    --figure-a: #f3d27a;
    --figure-b: #e9e2dc;
  }
  html, body {
    margin: 0;
    padding: 0;
    width: 1200px;
    height: 999px;
    overflow: hidden;
    background: var(--backdrop);
    font-family: "Open Sans", Arial, sans-serif;
  }
  .stage {
    position: relative;
    width: 1200px;
    height: 999px;
  }
  .card {
    position: absolute;
    width: 584px;
    height: 393px;
    background: var(--card);
    border-radius: 28px;
    overflow: hidden;
  }
  .card-front { left: 297px; top: 85px; }
  .card-back  { left: 302px; top: 517px; }

  .front-brand {
    position: absolute;
    left: 0; right: 0; top: 150px;
    display: flex;
    align-items: center;
    justify-content: center;
    gap: 16px;
  }
  .brand-dot {
    width: 40px; height: 40px;
    border-radius: 50%;
    background: var(--brand);
  }
  .brand-name {
    font-weight: 700;
    font-size: 64px;
    color: var(--brand);
    line-height: 1;
  }

  .swoosh {
    position: absolute;
    left: 0; top: 0;
  }
  .holder-name {
    position: absolute;
    left: 50px; top: 40px;
    margin: 0;
    font-weight: 700;
    font-size: 29px;
    color: var(--ink);
    letter-spacing: -0.3px;
  }
  .holder-title {
    position: absolute;
    left: 51px; top: 82px;
    margin: 0;
    font-size: 15px;
    letter-spacing: 2px;
    color: var(--ink);
  }
  .title-rule {
    position: absolute;
    left: 51px; top: 119px;
    width: 86px; height: 4px;
    background: var(--ink);
  }
  .back-brand {
    position: absolute;
    left: 420px; top: 48px;
    font-weight: 700;
    font-size: 22px;
    color: var(--ink);
  }
  .crew-illustration {
    position: absolute;
    left: 322px; top: 142px;
    width: 218px; height: 205px;
    border-radius: 14px;
    background: linear-gradient(135deg, var(--figure-a), var(--figure-b));
  }
  .contact {
    position: absolute;
    left: 50px; top: 267px;
    margin: 0;
    font-size: 20px;
    line-height: 30px;
    color: var(--ink);
    font-style: normal;
  }
</style>
</head>
<body>
<main class="stage">
  <section class="card card-front" aria-label="Card front">
    <div class="front-brand">
      <span class="brand-dot"></span>
      <span class="brand-name">BrickaFun</span>
    </div>
  </section>

  <section class="card card-back" aria-label="Card back">
    <svg class="swoosh" width="584" height="393" viewBox="0 0 584 393" aria-hidden="true">
      <defs>
        <linearGradient id="swooshFill" x1="0" y1="0" x2="1" y2="0.4">
          <stop offset="0" stop-color="var(--yellow-light)"/>
          <stop offset="1" stop-color="var(--yellow-deep)"/>
        </linearGradient>
      </defs>
      <path d="M0 0 H513 C420 18 330 75 255 145 C195 200 120 208 0 196 Z" fill="url(#swooshFill)"/>
      <path d="M200 0 H360 C300 30 250 80 215 130 C190 170 150 195 90 200 C160 180 185 140 200 100 C215 60 230 25 200 0 Z" fill="var(--yellow-deep)" opacity="0.35"/>
    </svg>
    <h1 class="holder-name">Dale Hurst</h1>
    <p class="holder-title">Co-Founder &amp; COO</p>
    <div class="title-rule"></div>
    <div class="back-brand">BrickaFun</div>
    <div class="crew-illustration" role="img" aria-label="Illustration of two cartoon construction workers in hard hats"></div>
    <address class="contact">
      (833) 517-BRICKAF<br>
      Dale@brickafun.com<br>
      www.brickafun.com
    </address>
  </section>
</main>
</body>
</html>
```